" Trata-se de empresa com vendas pelo telefone ou pela internet. Atualmente trabalhamos com toners e cartuchos porém no futuro vamos trabalhar com serviço de outsourcing de impressoras. "

```html
<!DOCTYPE html>
<html lang="pt-BR">
<head>
<meta charset="utf-8">
<title>Tonerlux – Papelaria</title>
<link rel="stylesheet" href="https://fonts.googleapis.com/css2?family=Montserrat:wght@600;700;800&family=Open+Sans:wght@400;600&display=swap">
<style>
  :root{
    --navy:#1c3d68;
    --navy-dark:#142e52;
    --teal:#2b9cc0;
    --sky:#cfe3ef;
    --paper:#ffffff;
    --ink:#3c4756;
    --muted:#8a96a6;
    --stage:#eceff2;
  }
  *{box-sizing:border-box;margin:0;padding:0}
  html,body{width:1200px;height:1200px;overflow:hidden;background:var(--stage)}
  body{position:relative;font-family:"Open Sans",Arial,sans-serif;color:var(--ink)}
  .item{position:absolute;box-shadow:0 6px 18px rgba(20,40,70,.25)}
  .brand{font-family:"Montserrat",Arial,sans-serif;font-weight:800;letter-spacing:.06em;display:flex;align-items:center;gap:.35em}
  .brand .dot{width:.7em;height:.7em;border-radius:50%;background:var(--teal);display:inline-block}
  .brand.light{color:#fff}
  .brand.dark{color:var(--navy)}
  .tagline{font-size:7px;color:var(--teal);letter-spacing:.03em}
  .small{font-size:7px;line-height:1.4}

  /* Folder */
  .folder{left:168px;top:89px;width:516px;height:392px;background:none;box-shadow:none}
  .folder-back{position:absolute;left:0;top:0;width:228px;height:535px}
  .folder-front{position:absolute;left:228px;top:0;width:288px;height:392px;background:var(--paper);box-shadow:0 6px 18px rgba(20,40,70,.25)}
  .folder-front .brand{position:absolute;left:60px;top:120px;font-size:26px}
  .folder-front .tagline{position:absolute;left:60px;top:155px;font-size:8px}
  .folder-front .web{position:absolute;right:24px;bottom:22px;font-size:9px;color:var(--navy);font-weight:600}
  .folder-back .brand{position:absolute;left:18px;top:180px;font-size:17px}
  .folder-back .tagline{position:absolute;left:18px;top:204px;color:var(--sky)}
  .folder-back .contact{position:absolute;top:265px;color:#fff;font-size:6.5px;line-height:1.4}

  /* Business cards */
  .card{width:156px;height:86px}
  .card-front{left:768px;top:372px;background:var(--paper);transform:rotate(-4deg)}
  .card-front .brand{position:absolute;left:34px;top:26px;font-size:13px}
  .card-front .tagline{position:absolute;left:34px;top:44px;font-size:5.5px}
  .card-front .stripe{position:absolute;left:0;right:0;bottom:0;height:16px;background:var(--navy);color:#fff;font-size:6px;padding:4px 8px}
  .card-back{left:840px;top:444px;background:var(--navy);color:#fff;transform:rotate(-4deg)}
  .card-back .brand{position:absolute;left:52px;top:10px;font-size:10px}
  .card-back .info{position:absolute;left:12px;top:30px;font-size:6px;line-height:1.5}
  .card-back .info b{font-size:7px}

  /* Pens */
  .pen{height:22px;width:290px;border-radius:11px 4px 4px 11px;display:flex;align-items:center;padding-left:90px}
  .pen .brand{font-size:9px}
  .pen-navy{left:828px;top:578px;background:linear-gradient(var(--navy),var(--navy-dark))}
  .pen-white{left:828px;top:626px;background:linear-gradient(#ffffff,#dfe5ec)}
  .pen::after{content:"";position:absolute;right:14px;top:4px;width:70px;height:4px;border-radius:2px;background:#c9d1da}

  /* Letterhead */
  .letter{left:432px;top:576px;width:276px;height:456px;background:var(--paper)}
  .letter .brand{position:absolute;left:36px;top:30px;font-size:13px}
  .letter .tagline{position:absolute;left:36px;top:47px;font-size:5.5px}
  .letter .head-contact{position:absolute;right:22px;top:28px;font-size:6px;line-height:1.5;text-align:right;color:var(--navy)}
  .letter .body{position:absolute;left:36px;right:28px;top:88px;font-size:6.5px;line-height:1.6;color:var(--muted)}
  .letter .body p{margin-bottom:10px}
  .letter .sign{position:absolute;right:30px;top:300px;font-size:6.5px;text-align:right;color:var(--ink)}
  .letter .foot{position:absolute;left:0;right:0;bottom:0;height:40px;background:linear-gradient(to right,var(--navy) 0 60%,var(--teal) 60% 100%)}
  .letter .foot-text{position:absolute;left:36px;bottom:48px;font-size:6px;color:var(--navy)}

  /* Compliment slip */
  .slip{left:96px;top:780px;width:312px;height:86px;background:var(--paper)}
  .slip .brand{position:absolute;left:20px;top:16px;font-size:13px}
  .slip .tagline{position:absolute;left:20px;top:33px;font-size:5.5px}
  .slip .info{position:absolute;right:24px;top:12px;font-size:6px;line-height:1.5;color:var(--ink)}
  .slip .info b{font-size:9px;color:var(--navy)}
  .slip .band{position:absolute;left:0;right:0;bottom:0;height:18px;background:linear-gradient(to right,var(--navy) 0 70%,var(--teal) 70% 100%)}

  /* Envelope */
  .envelope{left:792px;top:708px;width:336px;height:396px;box-shadow:none}
  .envelope svg{position:absolute;left:0;top:0;filter:drop-shadow(0 6px 12px rgba(20,40,70,.25))}
  .envelope .brand{position:absolute;font-size:13px}
  .env-front .brand{left:40px;top:128px}
  .env-front .info{position:absolute;left:40px;top:150px;font-size:6.5px;line-height:1.5;color:var(--navy)}
  .env-flip{position:absolute;left:130px;top:300px;transform:rotate(180deg)}
  .env-flip .brand{position:static;font-size:12px}
</style>
</head>
<body>

<!-- Folder -->
<section class="item folder">
  <div class="folder-back">
    <svg width="228" height="535" viewBox="0 0 228 535">
      <path d="M0 0H228V430Q150 470 110 510Q90 530 60 535L0 500Z" fill="var(--navy)"/>
    </svg>
    <div class="brand light">Tonerlux<span class="dot"></span></div>
    <div class="tagline">Soluções para sua impressão</div>
    <div class="contact" style="left:18px">Rua, número Bairro<br>Cidade/Estado</div>
    <div class="contact" style="left:140px">(11) 4000-2718<br>contato@tonerlux.com.br</div>
  </div>
  <div class="folder-front">
    <div class="brand dark">Tonerlux<span class="dot"></span></div>
    <div class="tagline">Soluções para sua impressão</div>
    <div class="web">www.tonerlux.com.br</div>
  </div>
</section>

<!-- Business cards -->
<section class="item card card-front">
  <div class="brand dark">Tonerlux<span class="dot"></span></div>
  <div class="tagline">Soluções para sua impressão</div>
  <div class="stripe">www.tonerlux.com.br</div>
</section>
<section class="item card card-back">
  <div class="brand light">Tonerlux<span class="dot"></span></div>
  <div class="info"><b>Nome Sobrenome</b><br>Diretor<br>(11) 4000-2718<br>contato@tonerlux.com.br<br>www.tonerlux.com.br</div>
</section>

<!-- Pens -->
<div class="item pen pen-navy"><span class="brand light">Tonerlux</span></div>
<div class="item pen pen-white"><span class="brand dark">Tonerlux</span></div>

<!-- Letterhead -->
<section class="item letter">
  <div class="brand dark">Tonerlux<span class="dot"></span></div>
  <div class="tagline">Soluções para sua impressão</div>
  <div class="head-contact">(11) 4000-2718<br>www.tonerlux.com.br<br>contato@tonerlux.com.br</div>
  <div class="body">
    <p>Prezado cliente, agradecemos a confiança em nossos produtos. Trabalhamos com toners e cartuchos de alta qualidade, entregues com rapidez em todo o país.</p>
    <p>Em breve ofereceremos também o serviço de outsourcing de impressoras, com manutenção, suprimentos e suporte técnico incluídos em um único contrato mensal.</p>
    <p>Ficamos à disposição para qualquer dúvida pelo telefone ou pelo nosso site.</p>
  </div>
  <div class="sign">Lucas Moreira<br><span style="color:var(--muted)">Diretor</span></div>
  <div class="foot-text">Rua, número Bairro &nbsp;&nbsp; Cidade/Estado</div>
  <div class="foot"></div>
</section>

<!-- Compliment slip -->
<section class="item slip">
  <div class="brand dark">Tonerlux<span class="dot"></span></div>
  <div class="tagline">Soluções para sua impressão</div>
  <div class="info"><b>Nome Sobrenome</b><br>Diretor<br>(11) 4000-2718<br>contato@tonerlux.com.br</div>
  <div class="band"></div>
</section>

<!-- Envelope -->
<section class="item envelope">
  <svg width="336" height="396" viewBox="0 0 336 396">
    <path d="M0 30Q0 0 40 0H296Q336 0 336 30L300 96H36Z" fill="var(--navy)"/>
    <rect x="0" y="96" width="336" height="114" fill="var(--paper)"/>
    <rect x="0" y="196" width="336" height="6" fill="var(--teal)"/>
    <rect x="0" y="202" width="336" height="8" fill="var(--navy)"/>
    <path d="M0 210H336V366Q336 396 306 396H30Q0 396 0 366Z" fill="var(--navy)"/>
    <path d="M0 210L168 300L336 210Z" fill="var(--navy-dark)" opacity=".5"/>
  </svg>
  <div class="env-front">
    <div class="brand dark">Tonerlux<span class="dot"></span></div>
    <div class="info">www.tonerlux.com.br<br>(11) 4000-2718</div>
  </div>
  <div class="env-flip"><div class="brand light">Tonerlux<span class="dot"></span></div></div>
</section>

</body>
</html>
```